Street Sign Project - Attract Customers

We need a street sign designed to display out the front of the building. It design will need to be 1800mm wide x 900mm high. We need to show potential customers where we are inviting. Some of the attachments are for inspiration. The sign will be printed on a sheet of aluminum. if you have a good look at our web site which is www.pk-r.com.au you should get a good feeling about the company and what we do.

Target Market(s)

Construction companies, landscaping and civil earth moving companies who may drive past our business

Industry/Entity Type

Building

Font styles to use
Sans Serif

Colors
ffffff
3277b5
000000

Requirements
Must have
• Company logo must be the main focus point
• The number "54" on the sign to show street number (300mm high)
• phone number - (02) 9418 3065
• web address - www.pk-r.com.au
• I have loaded pictures i would like to see used in the sign
Nice to have
• Banner picture as attached
Should not have
• Bright colours. Please use our blue colour where possible

```html
<!DOCTYPE html>
<html lang="en">
<head>
<meta charset="utf-8">
<title>Parker Rigging – Street Sign</title>
<link href="https://fonts.googleapis.com/css2?family=Arimo:wght@700&display=swap" rel="stylesheet">
<style>
  :root{
    --brand-blue:#1f73b7;
    --brand-blue-light:#3c88c6;
    --brand-blue-dark:#1767a9;
    --white:#ffffff;
    --black:#000000;
    --photo-roof:#9a5a4a;
    --photo-box:#8f97a3;
    --photo-worker:#6f7e8e;
  }
  html,body{margin:0;padding:0;width:1200px;height:999px;overflow:hidden;background:var(--black);}
  .canvas{position:relative;width:1200px;height:999px;font-family:"Arimo",Arial,sans-serif;}
  .sign{position:absolute;left:26px;top:212px;width:1148px;height:575px;overflow:hidden;background:var(--white);}
  .sign-art{position:absolute;inset:0;}
  .brand-name{
    position:absolute;left:62px;top:30px;margin:0;
    color:var(--brand-blue);font-weight:700;text-transform:uppercase;
    line-height:1;
  }
  .brand-name .line{display:block;font-size:100px;letter-spacing:1px;margin-bottom:2px;}
  .brand-name .suffix{display:block;font-size:24px;letter-spacing:4px;margin-top:6px;padding-left:6px;}
  .street-number{
    position:absolute;left:534px;top:348px;width:160px;text-align:center;
    color:var(--brand-blue);font-weight:700;font-size:98px;line-height:1;letter-spacing:-3px;
  }
  .phone{
    position:absolute;left:47px;top:442px;margin:0;
    color:var(--white);font-weight:700;font-size:66px;line-height:1;
  }
  .web{
    position:absolute;left:50px;top:522px;margin:0;
    color:var(--white);font-weight:700;font-size:44px;line-height:1;letter-spacing:3.5px;
  }
</style>
</head>
<body>
<div class="canvas">
  <section class="sign" aria-label="Parker Rigging street sign">
    <svg class="sign-art" width="1148" height="575" viewBox="0 0 1148 575" xmlns="http://www.w3.org/2000/svg">
      <defs>
        <linearGradient id="bandGradient" x1="0" y1="0" x2="0" y2="1">
          <stop offset="0" stop-color="var(--brand-blue-dark)"/>
          <stop offset="1" stop-color="var(--brand-blue-light)"/>
        </linearGradient>
        <linearGradient id="siteGradient" x1="0" y1="0" x2="0" y2="1">
          <stop offset="0" stop-color="#6f7d52"/>
          <stop offset="0.3" stop-color="#a58457"/>
          <stop offset="1" stop-color="#b7ab9a"/>
        </linearGradient>
      </defs>

      <path class="band" d="M0 243 C 180 330, 380 385, 560 395 L 560 575 L 0 575 Z" fill="url(#bandGradient)"/>
      <rect class="band" x="540" y="380" width="608" height="195" fill="url(#bandGradient)"/>
      <path class="swoosh" d="M0 300 C 180 375, 380 410, 560 412" fill="none" stroke="var(--white)" stroke-width="7"/>

      <path d="M700 0 L1148 0 L1148 425 L820 425 C 720 330, 690 150, 700 0 Z" fill="var(--brand-blue)"/>
      <path role="img" aria-label="Photo of a building site with a conveyor beside a timber fence"
            d="M716 0 L1148 0 L1148 410 L830 410 C 738 320, 708 150, 716 0 Z" fill="url(#siteGradient)"/>

      <circle cx="614" cy="398" r="88" fill="var(--brand-blue)"/>
      <circle cx="614" cy="398" r="76" fill="var(--white)"/>

      <circle cx="964" cy="378" r="140" fill="var(--brand-blue)"/>
      <circle cx="964" cy="378" r="130" fill="var(--white)"/>
      <circle role="img" aria-label="Photo of a worker on scaffolding with a hoist platform" cx="964" cy="378" r="124" fill="var(--photo-worker)"/>

      <circle cx="789" cy="300" r="102" fill="var(--brand-blue)"/>
      <circle cx="789" cy="300" r="93" fill="var(--white)"/>
      <circle role="img" aria-label="Photo of a ladder hoist on a tiled roof with solar panels" cx="789" cy="300" r="88" fill="var(--photo-roof)"/>

      <circle cx="809" cy="438" r="78" fill="var(--brand-blue)"/>
      <circle cx="809" cy="438" r="70" fill="var(--white)"/>
      <circle role="img" aria-label="Photo of a carton moving along a roller conveyor" cx="809" cy="438" r="65" fill="var(--photo-box)"/>

      <path d="M700 392 L716 388" stroke="var(--white)" stroke-width="5"/>
    </svg>

    <h1 class="brand-name">
      <span class="line">Parker</span>
      <span class="line">Rigging</span>
      <span class="suffix">Pty. Ltd.</span>
    </h1>

    <div class="street-number">54</div>

    <p class="phone">(02) 9418 3065</p>
    <p class="web">www.pk-r.com.au</p>
  </section>
</div>
</body>
</html>
```